Security Camera Sign

14” high x 11” wide Color: Blue, Yellow, Black and white

Make the sign vertical
Replace red with blue
WARNING: Black over yellow
These premises are protected by Closed Circuit Television: On white
Images are recorded for crime prevention and public safety. Unauthorized access, theft or vandalism will result in prosecution: On Blue

Target Market(s)

Outdoor commercial building

Industry/Entity Type

Security

Requirements
Nice to have
• I would like the sign stand out. If you need more colors? Thanks Ok

```html
<!DOCTYPE html>
<html lang="en">
<head>
<meta charset="utf-8">
<title>Security Camera Sign</title>
<link href="https://fonts.googleapis.com/css2?family=Archivo+Black&family=Archivo:wght@800&family=Arimo:wght@700&display=swap" rel="stylesheet">
<style>
  :root {
    --backdrop: #6f6f6f;
    --sign-blue: #2e3192;
    --signal-yellow: #fff200;
    --ink-black: #000000;
    --paper-white: #ffffff;
    --art-light: #e9e9e9;
    --art-dark: #4a4a4a;
  }
  html, body {
    margin: 0;
    padding: 0;
    width: 1200px;
    height: 1200px;
    overflow: hidden;
    background: var(--backdrop);
  }
  .sign {
    position: absolute;
    left: 207px;
    top: 90px;
    width: 786px;
    height: 1000px;
    border-radius: 34px;
    overflow: hidden;
    background: var(--paper-white);
    box-shadow: 0 34px 30px -10px rgba(0, 0, 0, 0.35);
  }
  .header-band {
    position: absolute;
    left: 0; top: 0;
    width: 100%;
    height: 150px;
    background: var(--sign-blue);
  }
  .warning-plate {
    position: absolute;
    left: 93px;
    top: 26px;
    width: 600px;
    height: 96px;
    box-sizing: border-box;
    background: var(--signal-yellow);
    border: 3px solid var(--ink-black);
    border-radius: 12px;
    display: flex;
    align-items: center;
    justify-content: center;
  }
  .warning-word {
    font-family: "Archivo Black", "Arial Black", sans-serif;
    font-size: 84px;
    line-height: 1;
    color: var(--ink-black);
    letter-spacing: 1px;
    margin-top: 4px;
  }
  .camera-art {
    position: absolute;
    left: 213px;
    top: 176px;
    width: 360px;
    height: 364px;
    border-radius: 8px;
    background: linear-gradient(135deg, var(--art-light) 0%, #bdbdbd 55%, var(--art-dark) 100%);
  }
  .cctv-notice {
    position: absolute;
    left: 0;
    top: 570px;
    width: 100%;
    margin: 0;
    text-align: center;
    font-family: "Archivo", "Arial Black", sans-serif;
    font-weight: 800;
    font-size: 48px;
    line-height: 56px;
    color: var(--sign-blue);
    text-transform: uppercase;
  }
  .footer-band {
    position: absolute;
    left: 0;
    bottom: 0;
    width: 100%;
    height: 176px;
    background: var(--sign-blue);
    display: flex;
    align-items: center;
    justify-content: center;
  }
  .legal-notice {
    margin: 0;
    text-align: center;
    font-family: "Arimo", Arial, sans-serif;
    font-weight: 700;
    font-size: 26px;
    line-height: 35px;
    color: var(--paper-white);
    text-transform: uppercase;
  }
</style>
</head>
<body>
  <div class="sign">
    <div class="header-band">
      <div class="warning-plate">
        <span class="warning-word">WARNING</span>
      </div>
    </div>

    <div class="camera-art" role="img" aria-label="Black and white line illustration of a wall-mounted security camera"></div>

    <p class="cctv-notice">These premises<br>are protected by<br>closed circuit<br>television</p>

    <div class="footer-band">
      <p class="legal-notice">Recorded for crime prevention<br>and public safety. Unauthorized<br>access, theft or vandalism will<br>result in prosecution</p>
    </div>
  </div>
</body>
</html>
```